Design Large Inspirational Artwork with Long Quote

Design a large piece of art with a quote from Marcus Tillwright.

QUOTE
"The thing that's so interesting about being alive is that you're all in. No matter what you do, you're all in. This is gonna kill you, so I think you might as well play the most magnificent game you can while you're waiting. Because, do you have anything better to do? Why not pick the best thing possible that you could do? Because you're more powerful than you think, way more powerful than you think. I mean, God only knows what you are in the final analysis. You're blind to your own weaknesses, but you're also blind to your own strengths. How far could you take that if you stopped wasting time, and if you stopped lying, and if you oriented yourself to the highest possible good that you could conceive of and you committed to that? How much good could you do? Well, I would say: why don't you find out?"

SIZE
A high-resolution print size of 6' wide and 3' tall should provide ample space for both the quote and the accompanying artwork.

TYPOGRAPHY
Choose a bold, clean, and easily readable font for the quote. You could also experiment with different font sizes for certain words or phrases to emphasize their importance within the quote.

COLORS
Since the quote is thought-provoking and reflective, you might want to use a color palette that evokes a sense of introspection and depth. Consider using cool, calming colors like shades of blue, gray, or green. Alternatively, you can use a contrasting color scheme with a light background and dark text to make the quote stand out.

ARTWORK
Select / create / edit background artwork to complement the quote.
While a great design might be minimalistic and/or greyscale, I'd really like to see some full color options. This might be anything from photography or graphics inspired by the ideas in the text, to abstract colors or illustrations that feel like the sentiment expressed.
The art should capture your attention and encourage you to read the text. The art should be visually appealing, both at a distance and up close, regardless of whether the text is read.
Updates

Having trouble confirming the exact print size.

Still looking for printing solution and final size confirmation.

Target Market(s)

Personal, business, office

Industry/Entity Type

None

Font styles to use
Sans Serif
Script

Requirements
Must have
• Entire quote, legible text, modern design, attractive artwork, approx 6ft wide and 3ft tall
Nice to have
• Different font (sizes) for certain words or phrases to emphasize their importance within the quote.

```html
<!DOCTYPE html>
<html lang="en">
<head>
<meta charset="utf-8">
<title>All In — Marcus Tillwright quote artwork</title>
<link href="https://fonts.googleapis.com/css2?family=Amatic+SC:wght@700&display=swap" rel="stylesheet">
<style>
  :root {
    --bg-top: #2c4b82;
    --bg-bottom: #1f6fc4;
    --ink: #ffffff;
    --highlight: #f7ee2c;
    --highlight-ink: #1c3d86;
    --mark-navy: #2a4777;
    --mark-sky: #2e9be3;
  }
  * { margin: 0; padding: 0; box-sizing: border-box; }
  html, body { width: 1200px; height: 600px; overflow: hidden; }
  body { background: var(--bg-bottom); }
  .artwork {
    position: relative;
    width: 1200px;
    height: 600px;
    overflow: hidden;
    background: linear-gradient(180deg, var(--bg-top) 0%, #25599f 50%, var(--bg-bottom) 100%);
  }
  .quote-marks {
    position: absolute;
    inset: 0;
    width: 1200px;
    height: 600px;
  }
  .quote-text {
    position: absolute;
    top: 30px;
    left: 0;
    width: 1200px;
    font-family: "Amatic SC", "Arial Narrow", sans-serif;
    font-weight: 700;
    font-size: 37px;
    line-height: 49.5px;
    color: var(--ink);
    text-transform: uppercase;
    letter-spacing: 0.2px;
  }
  .quote-line { display: block; white-space: nowrap; }
  .quote-line--indent { padding-left: 272px; }
  .quote-line--full { padding-left: 45px; }
  .emphasis {
    background: var(--highlight);
    color: var(--highlight-ink);
    padding: 0 3px;
    box-decoration-break: clone;
    -webkit-box-decoration-break: clone;
  }
</style>
</head>
<body>
<main class="artwork">
  <svg class="quote-marks" viewBox="0 0 1200 600" aria-hidden="true">
    <g class="quote-marks__open">
      <path fill="var(--mark-navy)" d="M112 68 C165 68 200 108 200 160 C200 240 150 300 80 332 C112 290 126 256 122 236 C74 232 40 200 40 150 C40 100 70 68 112 68 Z"/>
      <path fill="var(--mark-sky)" opacity="0.85" d="M200 58 C252 58 288 98 288 150 C288 230 238 290 168 322 C200 280 214 246 210 226 C162 222 128 190 128 140 C128 90 158 58 200 58 Z"/>
    </g>
    <g class="quote-marks__close">
      <path fill="var(--mark-sky)" d="M1002 380 C1050 380 1082 418 1082 466 C1082 540 1034 580 968 600 C996 566 1004 540 1000 522 C958 518 926 490 926 452 C926 410 960 380 1002 380 Z"/>
      <path fill="var(--mark-navy)" opacity="0.88" d="M1078 340 C1130 340 1166 380 1166 432 C1166 510 1116 560 1048 590 C1078 550 1090 520 1086 500 C1040 496 1004 466 1004 420 C1004 372 1036 340 1078 340 Z"/>
    </g>
  </svg>

  <p class="quote-text">
    <span class="quote-line quote-line--indent">The thing that's so interesting about <span class="emphasis">being alive</span> is that you're all in. No</span>
    <span class="quote-line quote-line--indent">matter what you do, you're all in. This is gonna kill you, so I think you</span>
    <span class="quote-line quote-line--indent">might as well play the most <span class="emphasis">magnificent game</span> you can while you're</span>
    <span class="quote-line quote-line--indent">waiting. Because, do you have <span class="emphasis">anything better</span> to do? Why not pick the</span>
    <span class="quote-line quote-line--full"><span class="emphasis">best thing possible</span> that you could do? Because you're <span class="emphasis">more powerful</span> than you think, way</span>
    <span class="quote-line quote-line--full">more powerful than you think. I mean, God only knows what you are in the <span class="emphasis">final analysis.</span></span>
    <span class="quote-line quote-line--full">You're blind to your <span class="emphasis">own weaknesses,</span> but you're also blind to your <span class="emphasis">own strengths.</span> How</span>
    <span class="quote-line quote-line--full">far could you take that if you <span class="emphasis">stopped wasting time,</span> and if you <span class="emphasis">stopped</span></span>
    <span class="quote-line quote-line--full"><span class="emphasis">lying,</span> and if you <span class="emphasis">oriented</span> yourself to the <span class="emphasis">highest possible good</span> that</span>
    <span class="quote-line quote-line--full">you could <span class="emphasis">conceive</span> of and you <span class="emphasis">committed</span> to that? How much good could</span>
    <span class="quote-line quote-line--full">you do? Well, I would say: <span class="emphasis">why don't you find out?</span></span>
  </p>
</main>
</body>
</html>
```